FACIAL COSMETICS BUSINESS CARD

WE ARE A DENTAL PRACTICE BUT ARE OPENING UP A BRANCH FOR FACILA COSMETICS, LIKE BOTOX, FILLERS, PEELS, ETC. MAEVE AND ISOLDA WILL BE RUNNING THAT PART OF THE BUSINESS.
OUR CURRENT CARD IS ATTACHED AND OUR LOGO IT ATTACHED TOO. THE LOGO HAS ON IT OVEN DENTAL, I WOULD LIKE IT TO SAY OVEN COSMETICS, THE PHONE NUMBERS ON IT HAS TO BE REPLACED BY THE ONES I GAVE PREVIOUSLY AND THE WEB ADDRESS HAS TO BE DELETED, THE OTHER SIDE OF THE CARD HAS A MAP WHICH HAS TO BE DELETED, ADD TWO DATE-TIME LINES, I LIKE THE CARDS TO BE SIMPLE AND CLEAN, SIZE HAS TO BE NO LARGER THAN 5CMx8.5CM.
THE CARD HAS TO BE MATTE, I HATE GLOSSY, ABLE TO BE WRITTEN ON BOTH SIDES

Updates
I HAVE ATTACHED THE FILES, THEY CONSIST OF OUR CURRENT LOGO IN A FEW FORMS AND OUR BUSINESS CARD FOR THE DENTAL BRANCH, PLEASE COPY THE CURRENT DESIGN BUT ADDING THE REQUESTED CHANGES

Industry/Entity Type
Business
Contact Information for Business Card
OVEN COSMETICS
MAEVE : 0438 572 913
ISOLDA : 0429 638 207
SUITE 8 COLWOOD PARK ARCADE
74-86 HALBERT STREET
COLWOOD PARK NSW 2284
Logo Text
OVEN COSMETICS
Look and feel

```html
<!DOCTYPE html>
<html lang="en">
<head>
<meta charset="utf-8">
<title>Oven Cosmetics – Business Card</title>
<link rel="stylesheet" href="https://fonts.googleapis.com/css2?family=Arimo:wght@400;700&display=swap">
<style>
  :root {
    --card-bg: #ffffff;
    --ink: #111111;
    --brand-green: #5cb946;
    --card-width: 1200px;
    --card-height: 693px;
  }
  html, body {
    margin: 0;
    padding: 0;
    width: var(--card-width);
    height: var(--card-height);
    overflow: hidden;
    background: var(--card-bg);
  }
  .business-card {
    position: relative;
    width: var(--card-width);
    height: var(--card-height);
    background: var(--card-bg);
    font-family: "Arimo", Arial, sans-serif;
    color: var(--ink);
    overflow: hidden;
  }
  .brand {
    position: absolute;
    left: 92px;
    top: 228px;
    display: flex;
    align-items: center;
    gap: 22px;
  }
  .brand-dot {
    width: 64px;
    height: 64px;
    border-radius: 50%;
    background: var(--brand-green);
    flex: none;
  }
  .brand-name {
    margin: 0;
    font-size: 46px;
    font-weight: 700;
    line-height: 1.05;
    letter-spacing: 3px;
    color: var(--ink);
  }
  .brand-name span { display: block; }
  .contact {
    position: absolute;
    left: 567px;
    top: 198px;
    font-size: 28.5px;
    letter-spacing: 1.2px;
  }
  .address {
    margin: 0;
    font-style: normal;
    font-weight: 700;
    line-height: 43px;
  }
  .phones {
    list-style: none;
    margin: 38px 0 0;
    padding: 0;
    font-weight: 400;
    line-height: 55px;
  }
  .phones .person { font-weight: 700; }
</style>
</head>
<body>
  <main class="business-card">
    <div class="brand">
      <div class="brand-dot" aria-hidden="true"></div>
      <h1 class="brand-name"><span>OVEN</span><span>COSMETICS</span></h1>
    </div>

    <section class="contact">
      <address class="address">
        Suite 8, Colwood Park Arcade<br>
        74-86 Halbert Street,<br>
        Colwood Park, NSW 2284
      </address>
      <ul class="phones">
        <li><span class="person">Maeve:</span> 0438 572 913</li>
        <li><span class="person">Isolda:</span> 0429 638 207</li>
      </ul>
    </section>
  </main>
</body>
</html>
```